Reed & Vale NC grand opening (for BILLBOARD)

Advertising the grand opening of our cannabis/hemp shop in NC. We will sell all things hemp (flower, cartridges, disposables, edibles, creams, lotions, pet products etc...)

Requirements
Must have
• include, open starting Aug 1, but grand opening Aug 15th.
Nice to have
• Difference slogan ideas "Save some cash, buy our grass" "Find your perfect high at Reed & Vale cannabis store" "Experience Nature's Gift: Reed & Vale Cannabis Store"

```html
<!DOCTYPE html>
<html lang="en">
<head>
<meta charset="utf-8">
<title>Reed &amp; Vale — Grand Opening Billboard</title>
<link rel="stylesheet" href="https://fonts.googleapis.com/css2?family=Montserrat:wght@700;900&family=Poppins:wght@500&display=swap">
<style>
  :root {
    --paper: #ffffff;
    --navy: #0d0d33;
    --lime: #7cc242;
    --leaf-dark: #3f7a14;
    --leaf-mid: #6da823;
    --leaf-light: #b4d843;
  }
  html, body {
    margin: 0;
    padding: 0;
    width: 1200px;
    height: 353px;
    overflow: hidden;
    background: var(--paper);
  }
  .billboard {
    position: relative;
    width: 1200px;
    height: 353px;
    background: var(--paper);
    overflow: hidden;
  }
  .edge-strip {
    position: absolute;
    left: 0;
    top: 0;
  }
  .brand-block {
    position: absolute;
    left: 58px;
    top: 70px;
  }
  .brand-name {
    margin: 0;
    font-family: "Poppins", sans-serif;
    font-weight: 500;
    font-size: 96px;
    line-height: 1;
    letter-spacing: -2px;
    color: var(--navy);
    white-space: nowrap;
  }
  .grand-opening {
    margin: 18px 0 0 4px;
    font-family: "Montserrat", sans-serif;
    font-weight: 900;
    font-size: 36px;
    line-height: 1;
    letter-spacing: 0.5px;
    color: var(--lime);
    white-space: nowrap;
  }
  .open-date {
    margin: 12px 0 0 5px;
    font-family: "Montserrat", sans-serif;
    font-weight: 700;
    font-size: 22px;
    line-height: 1;
    letter-spacing: 1px;
    color: var(--navy);
    text-transform: uppercase;
    white-space: nowrap;
  }
  .scene {
    position: absolute;
    inset: 0;
  }
  .exit-line {
    font-family: "Montserrat", sans-serif;
    font-weight: 900;
    fill: var(--paper);
  }
  .road-line {
    font-family: "Montserrat", sans-serif;
    font-weight: 700;
    fill: var(--paper);
  }
</style>
</head>
<body>
<main class="billboard">
  <svg class="edge-strip" width="10" height="353" viewBox="0 0 10 353" aria-hidden="true">
    <polygon points="0,0 8,0 8,168 0,160" fill="var(--lime)"/>
    <polygon points="0,172 8,180 8,353 0,353" fill="var(--navy)"/>
  </svg>

  <div class="brand-block">
    <h1 class="brand-name">Reed &amp; Vale</h1>
    <p class="grand-opening">GRAND OPENING AUG 15</p>
    <p class="open-date">Open starting Aug 1</p>
  </div>

  <svg class="scene" width="1200" height="353" viewBox="0 0 1200 353">
    <defs>
      <linearGradient id="foliage" x1="0" y1="0" x2="1" y2="1">
        <stop offset="0" stop-color="var(--leaf-mid)"/>
        <stop offset="0.45" stop-color="var(--leaf-light)"/>
        <stop offset="1" stop-color="var(--leaf-dark)"/>
      </linearGradient>
      <filter id="soft-shadow" x="-5%" y="-20%" width="110%" height="140%">
        <feDropShadow dx="1" dy="2" stdDeviation="1.5" flood-color="#000" flood-opacity="0.35"/>
      </filter>
    </defs>

    <path role="img" aria-label="Photo of fresh green hemp leaves"
          fill="url(#foliage)"
          d="M778,0 C860,0 892,60 889,122 C886,172 852,196 820,198 L760,200 C692,205 668,248 670,280 C672,322 702,350 760,353 L1200,353 L1200,0 Z"/>

    <path fill="var(--paper)"
          d="M715,228 C770,218 803,258 797,300 C792,332 772,350 757,353 L735,353 C764,330 772,292 752,262 C742,247 728,236 715,228 Z"/>

    <g filter="url(#soft-shadow)">
      <text class="exit-line" x="846" y="276" font-size="79" textLength="323" lengthAdjust="spacingAndGlyphs">EXIT 4B</text>
      <text class="road-line" x="848" y="317" font-size="41" textLength="321" lengthAdjust="spacingAndGlyphs">MAPLEGROVE RD</text>
    </g>
  </svg>
</main>
</body>
</html>
```